Crestline Slate & Tile Needs a Business Card

Attached you will find your logo, my photo and design guidelines for a new business card. The final design will need two separate files to create an embossed card. The cards will be printed by www.plinkprint.com (Instructions below)
Format is the Zib SQUARE card
Crestline Slate And Tile is a brick and mortar, retail stone and tile shop.
One the front:
Crestline Slate And Tile
Gerald Finchcombe
Owner
48207 Vesper Hollow Blvd
Suite R & T
Charlotte, NC 28953
Cell: 704-555-0183
Web: www.CrestlineSlateAndTile.com
(Make each word of the domain a different or alternating color)
On the back;
Something that shows beautiful colorful tile
Follow the design guide closely please. For more information see this page that describes creating the spot gloss file: https://www.plinkprint.com/us/business-cards/design-guidelines-spot-gloss
The logo is what we would like to have raised spot glossed.
Format is the Zib SQUARE card. See attahced guidlines.

```html
<!DOCTYPE html>
<html lang="en">
<head>
<meta charset="utf-8">
<title>Crestline Slate &amp; Tile – Square Business Card</title>
<link rel="stylesheet" href="https://fonts.googleapis.com/css2?family=Montserrat:wght@600&family=Mulish:wght@400;700&family=EB+Garamond:ital@1&display=swap">
<style>
  :root {
    --backdrop: #2c2c2d;
    --card-stock: #ecebe8;
    --ink-navy: #1d2a38;
    --ink-body: #2e3338;
    --accent-gold: #b8862e;
    --accent-rust: #b0502a;
    --accent-sage: #7c7f6e;
    --tile-navy: #1f2b3e;
    --tile-grey: #8d9096;
    --tile-sand: #c9b8a0;
  }
  html, body {
    margin: 0;
    padding: 0;
    width: 1200px;
    height: 1200px;
    overflow: hidden;
    background: var(--backdrop);
  }
  .canvas {
    position: relative;
    width: 1200px;
    height: 1200px;
  }
  .card {
    position: absolute;
    top: 300px;
    width: 545px;
    height: 628px;
  }
  .card-front {
    left: 36px;
    background: var(--card-stock);
    font-family: "Mulish", sans-serif;
    color: var(--ink-body);
    text-align: center;
  }
  .card-back {
    left: 617px;
    background:
      linear-gradient(135deg, var(--tile-grey) 0%, var(--tile-navy) 30%, var(--tile-sand) 55%, var(--tile-navy) 75%, var(--tile-grey) 100%);
  }
  .brand {
    position: absolute;
    top: 130px;
    left: 0;
    right: 0;
    display: flex;
    align-items: center;
    justify-content: center;
    gap: 22px;
  }
  .brand-square {
    width: 84px;
    height: 84px;
    background: var(--ink-navy);
  }
  .brand-name {
    font-family: "Mulish", sans-serif;
    font-weight: 400;
    font-size: 34px;
    line-height: 1.15;
    letter-spacing: 4px;
    text-transform: uppercase;
    color: var(--ink-navy);
    text-align: left;
  }
  .owner-name {
    position: absolute;
    top: 282px;
    left: 0;
    right: 0;
    font-family: "Montserrat", sans-serif;
    font-weight: 600;
    font-size: 25px;
    letter-spacing: 3px;
    color: var(--ink-navy);
  }
  .owner-title {
    position: absolute;
    top: 318px;
    left: 0;
    right: 0;
    font-family: "EB Garamond", serif;
    font-style: italic;
    font-size: 19px;
    color: var(--ink-body);
  }
  .address {
    position: absolute;
    top: 356px;
    left: 0;
    right: 0;
    font-style: normal;
    font-size: 19px;
    line-height: 26px;
  }
  .divider {
    position: absolute;
    top: 447px;
    left: 172px;
    width: 208px;
    height: 1.5px;
    background: var(--accent-gold);
    border: 0;
    margin: 0;
  }
  .contact {
    position: absolute;
    left: 0;
    right: 0;
    font-size: 21px;
  }
  .contact b { color: var(--ink-navy); font-weight: 700; }
  .contact-cell { top: 477px; }
  .contact-web { top: 527px; }
  .web-crestline { color: var(--accent-gold); font-weight: 700; }
  .web-slate { color: var(--ink-navy); font-weight: 700; }
  .web-and { color: var(--accent-sage); font-weight: 700; }
  .web-tile { color: var(--accent-rust); font-weight: 700; }
</style>
</head>
<body>
<main class="canvas">
  <section class="card card-front" aria-label="Business card front">
    <div class="brand">
      <div class="brand-square" aria-hidden="true"></div>
      <div class="brand-name">Crestline<br>Slate &amp; Tile</div>
    </div>
    <div class="owner-name">GERALD FINCHCOMBE</div>
    <div class="owner-title">Owner</div>
    <address class="address">
      48207 Vesper Hollow Blvd<br>
      Suite R &amp; T<br>
      Charlotte, NC 28953
    </address>
    <hr class="divider">
    <div class="contact contact-cell"><b>Cell:</b> 704-555-0183</div>
    <div class="contact contact-web"><b>Web: www.</b><span class="web-crestline">Crestline</span><span class="web-slate">Slate</span><span class="web-and">And</span><span class="web-tile">Tile</span>.com</div>
  </section>
  <section class="card card-back" role="img" aria-label="Mosaic of marble and patterned tiles in navy, grey and sand laid on the diagonal"></section>
</main>
</body>
</html>
```